依頼詳細
・サイズ:
シート看板 1800×6000(縦でも横でも可)
(建築現場での広告のため車で前面道路を通っても伝わるようなデザイン)

キャッチコピーとしては「建築相談受付中」や「土地活用無料相談」などのアパート建築に係る内容を検討して頂ければと思います。
記載項目
会社名/ヒサノホーム株式会社
電話番号/098-631-2947
(ロゴを添付)
希望イメージ
シンプル 複雑
単色 カラフル
暗い 明るい
日常 高級
遊び心 厳粛
未来的 伝統的
女性的 男性的
希望する色
赤系、黄・オレンジ系、緑系
補足説明
まずはデザインを出していただき、詳細はデザイン決定後
打ち合わせをしながら進めさせて頂きたいです。

その他ご質問等ありましたら、気軽にお問い合わせください。
ご応募をお待ちしております!

シンプルでイメージに合った提案だった。修正対応も迅速で丁寧に対応して頂いた。

今回はご提案き誠にありがとうございました。今後も広告等のデザイン作成依頼を予定しておりますのでご参加いただけると幸いです。

```html
<!DOCTYPE html>
<html lang="ja">
<head>
<meta charset="utf-8">
<title>ヒサノホーム 建築相談受付中</title>
<link rel="stylesheet" href="https://fonts.googleapis.com/css2?family=Noto+Serif+JP:wght@700;900&family=Noto+Sans+JP:wght@500;700&family=Montserrat:wght@500;700&display=swap">
<style>
  :root {
    --orange: #e6551b;
    --white: #ffffff;
    --shadow: #d9d9d9;
    --ink: #1a1a1a;
    --gold: #b39a63;
  }
  html, body { margin: 0; padding: 0; overflow: hidden; }
  .sign {
    position: relative;
    width: 1200px;
    height: 3996px;
    background: var(--orange);
    overflow: hidden;
    color: var(--white);
  }
  .swoosh { position: absolute; left: 0; top: 0; }
  .brand {
    position: absolute; top: 150px; left: 0; width: 100%;
    text-align: center;
  }
  .brand-mark {
    width: 420px; height: 420px; margin: 0 auto;
    border: 22px solid var(--white); border-radius: 50%; box-sizing: border-box;
  }
  .brand-name {
    margin-top: 70px;
    font-family: "Montserrat", sans-serif; font-weight: 500;
    font-size: 76px; letter-spacing: 8px;
  }
  .audience {
    position: absolute; top: 1020px; left: 160px; width: 880px;
    font-family: "Noto Serif JP", serif; font-weight: 700;
    font-size: 66px; text-align: center;
  }
  .audience p { margin: 0; line-height: 100px; }
  .audience .rule { height: 4px; background: var(--white); margin: 22px 0; }
  .headline {
    position: absolute; top: 1360px; left: 700px; width: 320px;
    font-family: "Noto Serif JP", serif; font-weight: 900;
    font-size: 300px; line-height: 375px; text-align: center;
  }
  .status {
    position: absolute; top: 1930px; left: 230px; width: 310px;
    font-family: "Noto Serif JP", serif; font-weight: 900;
  }
  .status span {
    display: block; height: 310px; margin-bottom: 24px;
    background: var(--white); color: var(--orange);
    font-size: 260px; line-height: 310px; text-align: center;
  }
  .company {
    position: absolute; top: 3560px; left: 0; width: 100%;
    display: flex; justify-content: center; align-items: center; gap: 18px;
    color: var(--ink);
    font-family: "Noto Sans JP", sans-serif; font-weight: 500;
  }
  .company .name { font-size: 140px; letter-spacing: 4px; }
  .company .type { font-size: 62px; line-height: 66px; width: 130px; text-align: center; }
  .phone {
    position: absolute; top: 3770px; left: 0; width: 100%;
    display: flex; justify-content: center; align-items: center; gap: 20px;
    color: var(--gold);
    font-family: "Montserrat", sans-serif; font-weight: 700; font-size: 132px;
  }
</style>
</head>
<body>
<main class="sign">
  <svg class="swoosh" width="1200" height="3996" viewBox="0 0 1200 3996">
    <path d="M0 2990 Q 260 3420 1200 3470 L1200 3996 L0 3996 Z" fill="var(--shadow)"/>
    <path d="M0 3050 Q 320 3470 1200 3520 L1200 3996 L0 3996 Z" fill="var(--white)"/>
  </svg>

  <header class="brand">
    <div class="brand-mark"></div>
    <div class="brand-name">HISANO HOME</div>
  </header>

  <section class="audience">
    <p>アパート用地をお持ちの方</p>
    <div class="rule"></div>
    <p>建て替えをご検討の方</p>
  </section>

  <h1 class="headline">建<br>築<br>相<br>談</h1>

  <div class="status"><span>受</span><span>付</span><span>中</span></div>

  <div class="company">
    <span class="name">ヒサノホーム</span>
    <span class="type">株式<br>会社</span>
  </div>

  <div class="phone">
    <svg width="110" height="110" viewBox="0 0 24 24" fill="none" stroke="var(--gold)" stroke-width="2" stroke-linecap="round" stroke-linejoin="round">
      <path d="M22 16.9v3a2 2 0 0 1-2.2 2 19.8 19.8 0 0 1-8.6-3.1 19.5 19.5 0 0 1-6-6A19.8 19.8 0 0 1 2.1 4.2 2 2 0 0 1 4.1 2h3a2 2 0 0 1 2 1.7c.1 1 .4 1.9.7 2.8a2 2 0 0 1-.5 2.1L8 9.9a16 16 0 0 0 6 6l1.3-1.3a2 2 0 0 1 2.1-.4c.9.3 1.8.6 2.8.7a2 2 0 0 1 1.7 2z"/>
      <path d="M15 2a7 7 0 0 1 7 7M15 6a3 3 0 0 1 3 3"/>
    </svg>
    <span>098-631-2947</span>
  </div>
</main>
</body>
</html>
```